Business Card For Talent Company
BLITZ Talent
Project: Business Card For Talent Company
Business Card For Talent Company - Entertainment
Creative Brief
Cutting-Edge
Lorna Pidge
Talent Development
2734 W. Ferncastle Rd. Dovermill Park IL 60419
blitztalent@quorvex.com
www.blitztalent-quorvex.com
Are you ready to break through?
Kelvorn Kelvorn
We are really desperate to see some fun contemporary and modern designs...we are a talent company...would really like to see something innovative and not so corporate looking.....thank you!
Aquamarine/Teal Shade of Blue Please!....We really want something fun and edgy....these are too corporate looking...
We are a talent agency....really looking for something cool and cutting edge for our company...the shade of blue is coming through wrong on the logo...we are looking for a more like a teal blue color....thank you!
Our Tag Line "are you ready to break through" needs to be on all of the materials....thank you!
we are looking for more of teal shade of blue..I uploaded our other logo....
This contest is for full stationary...
It is both business card and stationary that we are needing....thank you!

```html
<!DOCTYPE html>
<html lang="en">
<head>
<meta charset="utf-8">
<title>BLITZ Talent Stationery</title>
<link href="https://fonts.googleapis.com/css2?family=Roboto:wght@400;900&display=swap" rel="stylesheet">
<style>
:root{
  --ink:#111214;
  --paper:#ffffff;
  --teal:#1cc3c9;
  --blue:#2154a6;
  --rule:#c9cdd2;
  --grey:#555a60;
}
*{margin:0;padding:0;box-sizing:border-box}
html,body{width:1200px;height:886px;overflow:hidden;background:var(--paper)}
body{position:relative;font-family:"Roboto",Arial,sans-serif;color:var(--ink)}
.piece{position:absolute;background:var(--paper);box-shadow:0 0 0 1px var(--rule);overflow:hidden}
.brand{font-weight:900;letter-spacing:.06em;text-transform:uppercase;white-space:nowrap;line-height:1}
.brand.on-dark{color:var(--paper)}
.band{position:absolute;left:0;right:0;background:var(--ink)}
.pattern{position:absolute;background:linear-gradient(100deg,#111214 0%,#1d2e36 45%,#111214 100%)}
.fine{position:absolute;font-size:6px;color:var(--grey);line-height:1.4;white-space:nowrap}
.fine.light{color:#cfd4d8}
.mark-dot{display:inline-block;width:14px;height:14px;border-radius:50%;background:linear-gradient(135deg,var(--teal),var(--blue));vertical-align:middle;margin-right:6px}

/* round sticker */
.sticker{left:98px;top:67px;width:164px;height:164px;border-radius:50%;box-shadow:none;border:2px solid var(--teal);display:flex;align-items:center;justify-content:center;flex-direction:column}
.sticker .brand{font-size:30px}
.sticker .sub{font-size:10px;font-weight:900;letter-spacing:.5em;margin-top:4px}

/* envelope flap (top) */
.flap-env{left:300px;top:24px;width:192px;height:192px}
.flap-env .mirror{top:18px;height:36px;display:flex;align-items:center;justify-content:center;transform:scaleY(-1)}
.flap-env .front{top:144px;height:48px;display:flex;align-items:center;justify-content:center}
.flap-env .brand{font-size:22px}

/* business cards */
.card-front{left:36px;top:283px;width:132px;height:65px}
.card-front .band{top:0;height:18px}
.card-front .fine{font-size:5px}
.card-front .contact{right:6px;text-align:right}
.card-back{left:36px;top:365px;width:132px;height:80px;background:var(--ink)}
.card-back .brand{position:absolute;left:10px;top:22px;font-size:20px}

/* letterhead */
.letterhead{left:180px;top:283px;width:317px;height:384px}
.letterhead .band.head{top:0;height:64px}
.letterhead .band.head .brand{position:absolute;left:34px;top:18px;font-size:32px}
.letterhead .band.foot{bottom:14px;height:14px}

/* folder */
.folder-left{left:509px;top:101px;width:322px;height:540px}
.folder-left .return{position:absolute;left:0;right:0;top:360px;text-align:center;font-size:6px;color:var(--grey);line-height:1.5}
.folder-left .return .mark-dot{display:block;margin:0 auto 8px}
.folder-right{left:831px;top:101px;width:333px;height:460px}
.folder-right .band.head{top:0;height:79px}
.folder-right .band.head .brand{position:absolute;right:24px;top:18px;font-size:34px}
.folder-right .band.mid{top:298px;height:144px}
.folder-right .emblem{position:absolute;left:50%;top:330px;transform:translate(-50%,-50%);width:128px;height:128px;border-radius:50%;background:linear-gradient(160deg,var(--teal),var(--blue))}
.pocket{position:absolute;left:831px;top:540px;width:333px;height:156px;background:var(--paper);box-shadow:0 0 0 1px var(--rule)}
.folder-tabs{position:absolute;left:509px;top:540px;width:322px;height:156px}

/* lower envelope */
.envelope{left:144px;top:696px;width:348px;height:163px}
.envelope .emblem-band{position:absolute;left:0;top:30px;width:60px;height:90px;background:linear-gradient(180deg,var(--teal),var(--blue))}
.envelope .brand{position:absolute;left:100px;top:14px;font-size:28px}
.envelope .sub{position:absolute;left:130px;top:46px;font-size:8px;font-weight:900;letter-spacing:.6em}
.envelope .band{top:62px;height:64px;left:60px}

/* envelope back */
.env-back{left:509px;top:696px;width:343px;height:163px}
.env-back .brand{position:absolute;left:0;right:0;top:8px;text-align:center;font-size:22px}

/* small compliment card */
.comp{left:869px;top:696px;width:300px;height:67px}
.comp .band{top:0;height:22px}
.comp .brand{position:absolute;left:10px;top:5px;font-size:13px}
</style>
</head>
<body>

<div class="piece sticker">
  <span class="brand">Blitz</span>
  <span class="sub">TALENT</span>
</div>

<div class="piece flap-env">
  <div class="band mirror"><span class="brand on-dark">Blitz</span></div>
  <div class="band front"><span class="brand on-dark">Blitz Talent</span></div>
</div>

<div class="piece card-front">
  <div class="band"></div>
  <div class="fine" style="left:7px;top:24px;font-weight:900;color:var(--ink)">Lorna Pidge</div>
  <div class="fine" style="left:7px;top:31px">Talent Development</div>
  <div class="fine contact" style="top:24px">(555) 014-2290</div>
  <div class="fine contact" style="top:31px">blitztalent@quorvex.com</div>
  <div class="fine contact" style="top:38px">www.blitztalent-quorvex.com</div>
</div>

<div class="piece card-back">
  <span class="brand on-dark">Blitz</span>
  <div class="fine light" style="left:10px;top:52px">Are you ready to break through?</div>
</div>

<div class="piece letterhead">
  <div class="band head">
    <div class="pattern" role="img" aria-label="Abstract circuit pattern" style="inset:0"></div>
    <span class="brand on-dark">Blitz Talent</span>
  </div>
  <div class="band foot">
    <div class="fine light" style="left:8px;top:4px">2734 W. Ferncastle Rd. Dovermill Park IL 60419</div>
    <div class="fine light" style="right:8px;top:4px">www.blitztalent-quorvex.com</div>
  </div>
</div>

<div class="piece folder-left">
  <div class="return">
    <span class="mark-dot"></span>
    2734 W. Ferncastle Rd.<br>Dovermill Park IL 60419<br>www.blitztalent-quorvex.com
  </div>
</div>

<div class="piece folder-right">
  <div class="band head">
    <div class="pattern" role="img" aria-label="Abstract circuit pattern" style="inset:0"></div>
    <span class="brand on-dark">Blitz</span>
  </div>
  <div class="band mid"></div>
  <div class="emblem"></div>
</div>

<svg class="folder-tabs" viewBox="0 0 322 156" aria-hidden="true">
  <path d="M0 0 H322 V156 H40 L0 110 Z" fill="none" stroke="#c9cdd2"/>
</svg>
<div class="pocket">
  <svg width="333" height="156" viewBox="0 0 333 156" aria-hidden="true">
    <path d="M110 40 l30 -30 l30 30 l-30 30 z" fill="none" stroke="#c9cdd2" stroke-dasharray="4 3"/>
  </svg>
</div>

<div class="piece envelope">
  <div class="emblem-band"></div>
  <span class="brand">Blitz</span>
  <span class="sub">TALENT</span>
  <div class="band">
    <div class="pattern" role="img" aria-label="Abstract circuit pattern" style="inset:0"></div>
  </div>
  <div class="fine" style="left:110px;top:136px">2734 W. Ferncastle Rd. Dovermill Park IL 60419</div>
</div>

<div class="piece env-back">
  <svg width="343" height="70" viewBox="0 0 343 70" style="position:absolute;left:0;top:0" aria-hidden="true">
    <path d="M0 0 H343 V28 Q171 70 0 28 Z" fill="#111214"/>
  </svg>
  <span class="brand on-dark">Blitz</span>
  <div class="fine" style="left:0;right:0;top:150px;text-align:center">www.blitztalent-quorvex.com</div>
</div>

<div class="piece comp">
  <div class="band"><span class="brand on-dark">Blitz</span></div>
  <div class="fine" style="left:10px;top:30px">Are you ready to break through?</div>
  <div class="fine" style="right:10px;top:30px">blitztalent@quorvex.com</div>
</div>

</body>
</html>
```